Volren Goods Ltd Stationery Design Project

hi we need to design business cards, letter head, complimentary slips, scribble pads, note pads, envelopes for volren goods ltd.

please see business cards details

Kelvin Obutu

P.O Box 41873 -00312 Nairobi - Kenya
Tel: +254-733-218-904
Email: volrengoods@mailvexo.com

company name should appear on all stationery : Volren Goods Ltd

Industry/Entity Type

Business

Requirements
Must have
• kindly stick to colours in the logo

```html
<!DOCTYPE html>
<html lang="en">
<head>
<meta charset="utf-8">
<title>Volren Goods Ltd – Note Pad</title>
<link rel="stylesheet" href="https://fonts.googleapis.com/css2?family=Open+Sans:wght@600;700&display=swap">
<style>
  :root {
    --brand-orange: #f39a1e;
    --brand-blue: #2b3990;
    --rule-dark: #3a3a3a;
    --rule-light: #c9c9c9;
    --paper: #ffffff;
  }
  html, body {
    margin: 0;
    padding: 0;
    width: 800px;
    height: 1200px;
    overflow: hidden;
    background: var(--paper);
  }
  .notepad {
    position: relative;
    width: 800px;
    height: 1200px;
    background: var(--paper);
    font-family: "Open Sans", Arial, sans-serif;
  }
  .brand {
    position: absolute;
    left: 32px;
    top: 42px;
    display: flex;
    align-items: center;
    gap: 8px;
  }
  .brand-dot {
    width: 14px;
    height: 14px;
    border-radius: 50%;
    background: var(--brand-orange);
  }
  .brand-name {
    font-size: 27px;
    font-weight: 700;
    letter-spacing: 0.5px;
    color: var(--brand-orange);
    line-height: 1;
  }
  .company-name {
    position: absolute;
    left: 39px;
    top: 86px;
    font-size: 13px;
    font-weight: 600;
    color: var(--brand-blue);
  }
  .date-field {
    position: absolute;
    left: 651px;
    top: 123px;
    display: flex;
    align-items: flex-end;
    font-size: 10px;
    font-weight: 700;
    color: var(--brand-blue);
  }
  .date-line {
    display: inline-block;
    width: 100px;
    margin-left: 3px;
    border-bottom: 1px solid var(--brand-blue);
  }
  .header-rule {
    position: absolute;
    left: 0;
    top: 137px;
    width: 800px;
    height: 2px;
    border-top: 1px solid var(--rule-dark);
    border-bottom: 1px solid var(--rule-dark);
  }
  .writing-lines {
    position: absolute;
    left: 0;
    top: 146px;
    width: 800px;
    height: 976px;
    background: repeating-linear-gradient(
      to bottom,
      transparent 0,
      transparent 36.5px,
      var(--rule-light) 36.5px,
      var(--rule-light) 37.5px
    );
  }
</style>
</head>
<body>
  <main class="notepad">
    <div class="brand">
      <span class="brand-dot"></span>
      <span class="brand-name">VOLREN GOODS</span>
    </div>
    <div class="company-name">Volren Goods Ltd</div>
    <div class="date-field">Date:<span class="date-line"></span></div>
    <div class="header-rule"></div>
    <div class="writing-lines"></div>
  </main>
</body>
</html>
```